New Web-Page Design Required

We need a new or initial web design for our page varno-labs.com. We provide products & services around infrastructure products. We have two products at the moment, but another 2 in the pipeline.
We want to have the following page structure (and part of the project is to design the 7 pages):
- Home
- Products
-One page per product
- Service
- Support
- About
- Contact (Email form)
The start page should include the following information:
- Twitter / Linkedin Links
- Telephone / Email or in general contact details
- News
- Maybe a link-box, where we can highlight/showcase things
- Link to our support portal, quite prominent
- Testimonials
It would be nice if the product pages would have a image header, where we can put up a screenshot or something. Links to datasheet and videos of the product would be nice as well.
We like the "big banner in the middle" designs, like these two Joomla examples. No need to copy them, it should just give you an idea.
http://www.plumeforge.com/itempreview/185
http://www.plumeforge.com/content/asj42/index.php
Budget for images available, so please use placeholders or ask us for specific photos/images, if you need them for your design.
Target Market(s)
Business-2-Business, Decision makers and Technical Leads
Industry/Entity Type
News
Look and feel
Each slider illustrates characteristics of the customer's brand and the style your logo design should communicate.

```html
<!DOCTYPE html>
<html lang="en">
<head>
<meta charset="utf-8">
<title>Varno-Labs — Home</title>
<link rel="stylesheet" href="https://fonts.googleapis.com/css2?family=Fjalla+One&family=Open+Sans:ital,wght@0,400;0,600;1,400&display=swap">
<style>
:root{
  --teal:#14b3c4;
  --teal-dark:#0e8f9c;
  --ink:#2a2627;
  --ink-2:#3a3637;
  --grey-tab:#6d6b6b;
  --grey-head:#e6e6e6;
  --grey-band:#dcdcdc;
  --nav-bg:#efefef;
  --line:#c9c9c9;
  --text:#333;
  --white:#fff;
  --page:#f3f3f3;
}
*{box-sizing:border-box;margin:0;padding:0}
html,body{width:1118px;height:1200px;overflow:hidden}
body{background:var(--page);font-family:"Open Sans",Verdana,sans-serif;color:var(--text);position:relative}
.abs{position:absolute}
/* header */
.logo-box{left:169px;top:12px;width:168px;height:84px;border:3px solid #d6d6d6;background:var(--white);display:flex;align-items:center;justify-content:center;gap:8px}
.logo-mark{width:28px;height:28px;border-radius:50%;background:var(--teal-dark)}
.logo-name{font-size:22px;font-weight:600;color:#4a4a4a}
.contact{left:766px;top:30px;font-size:12px;line-height:14px;color:#222}
.social{left:766px;top:64px;display:flex;gap:6px}
.social a{width:25px;height:25px;border:2px solid #d6d6d6;background:var(--teal-dark);display:block}
/* nav */
.nav{left:0;top:103px;width:1118px;height:37px;background:var(--nav-bg);border-top:1px solid var(--line);border-bottom:1px solid var(--line)}
.nav-list{position:absolute;left:169px;top:0;height:36px;display:flex;list-style:none}
.nav-list li{height:36px;width:99px;border-right:1px solid var(--line);font-family:"Fjalla One",sans-serif;font-size:12px;letter-spacing:1px;display:flex;align-items:center;justify-content:center;color:#222}
.nav-list li.home{width:46px;background:var(--ink)}
.nav-list li.active{background:var(--ink);color:var(--white);outline:2px solid #888;outline-offset:-3px}
.dropdown{left:415px;top:140px;width:149px;height:53px;background:#5a5756;color:#f0f0f0;font-size:15px;letter-spacing:.5px;padding:15px 12px 0}
.dropdown span{border-bottom:1px solid #aaa;padding-bottom:2px}
.dropdown::before{content:"";position:absolute;left:34px;top:-6px;border:6px solid transparent;border-top:0;border-bottom-color:#5a5756}
/* hero */
.hero{left:0;top:140px;width:1118px;height:337px;background:var(--ink);border-bottom:5px solid var(--teal-dark)}
.hero-visual{left:169px;top:0;width:547px;height:332px;background:linear-gradient(160deg,#c9c2b8 0%,#8e8a86 30%,#2b2d30 55%,#4a4c50 80%,#d6cdbd 100%)}
.slide-tabs{left:716px;top:3px;display:flex}
.slide-tabs span{width:46px;height:44px;background:var(--grey-tab);color:var(--white);font-family:"Fjalla One",sans-serif;font-size:22px;display:flex;align-items:center;justify-content:center;position:relative}
.slide-tabs span.current{background:var(--teal)}
.slide-tabs span.current::after{content:"";position:absolute;bottom:-10px;left:13px;border:10px solid transparent;border-bottom:0;border-top-color:var(--teal)}
.hero-title{left:716px;top:82px;width:183px;text-align:center;font-family:"Fjalla One",sans-serif;color:var(--white)}
.hero-title h1{font-size:31px;font-weight:400;line-height:38px}
.hero-title h2{font-size:22px;font-weight:400;line-height:30px}
.hero-copy{left:732px;top:184px;width:185px;font-family:"Fjalla One",sans-serif;font-size:12.5px;line-height:18px;color:#eee;letter-spacing:.3px}
/* columns */
.col{top:528px;width:183px}
.col-head{height:38px;background:var(--grey-head);font-family:"Fjalla One",sans-serif;font-weight:400;font-size:15px;letter-spacing:1px;color:#222;padding:9px 8px}
.videos{background:var(--ink-2);margin-top:6px;height:252px;padding:12px 10px;color:var(--white)}
.videos li{list-style:none;margin-bottom:14px}
.videos b{font-weight:400;font-size:14px;display:block;margin-bottom:2px}
.videos b::before{content:"›";font-weight:600;margin-right:7px}
.videos small{font-size:11px;line-height:14px;display:block}
.support-photo{margin-top:6px;height:115px;border:1px solid #ccc;background:linear-gradient(135deg,#e9e6e2,#c9b8a6 55%,#f4f4f4)}
.support-box{margin-top:8px;height:128px;background:var(--teal);padding:14px 6px 0;font-size:11px;line-height:13.5px;color:#123}
.btn{display:inline-block;margin-top:12px;background:var(--white);font-family:"Fjalla One",sans-serif;font-size:12px;letter-spacing:.5px;padding:3px 8px;color:#222}
.news{padding:5px 2px}
.news h3{font-family:"Fjalla One",sans-serif;font-weight:400;font-size:13px;margin-top:6px}
.news time{font-family:"Fjalla One",sans-serif;font-size:10px;display:block;margin:2px 0 6px}
.news p{font-size:10px;line-height:14px;margin-bottom:14px}
.quote{position:relative;margin-top:10px;height:106px;background:var(--ink-2);border-radius:10px;color:var(--white);padding:24px 14px 0 30px;box-shadow:0 3px 5px rgba(0,0,0,.3)}
.quote p{font-style:italic;font-size:12px;line-height:14px;letter-spacing:.3px}
.quote cite{display:block;font-style:normal;font-weight:600;font-size:11.5px;margin-top:6px;letter-spacing:.5px}
.quote .mark{position:absolute;font-family:Georgia,serif;font-size:34px;line-height:1;color:#777}
.quote .mark.open{left:14px;top:14px}
.quote .mark.close{left:86px;top:54px}
.quote::after{content:"";position:absolute;left:88px;bottom:-14px;border-right:38px solid transparent;border-top:15px solid var(--ink-2)}
/* gallery */
.gallery{left:0;top:871px;width:1118px;height:245px;background:var(--grey-band)}
.gallery-label{left:218px;top:6px;background:var(--ink);color:var(--white);font-family:"Fjalla One",sans-serif;font-weight:400;font-size:18px;letter-spacing:1px;padding:3px 14px}
.thumb{top:70px;width:151px;height:112px;background:linear-gradient(180deg,#2c3034,#1f2326);box-shadow:0 2px 4px rgba(0,0,0,.35)}
.arrow{top:95px}
/* footer */
.footer{left:0;top:1116px;width:1118px;height:84px;background:var(--ink);color:var(--white);text-align:center;font-size:12.5px;line-height:21px;padding-top:25px;letter-spacing:.3px}
</style>
</head>
<body>
<header>
  <div class="abs logo-box"><span class="logo-mark"></span><span class="logo-name">varno-labs</span></div>
  <div class="abs contact">Phone- 0123 4567 8900<br>Email-&nbsp; info@varno-labs.com</div>
  <div class="abs social"><a href="#" aria-label="Professional network"></a><a href="#" aria-label="Microblog"></a></div>
</header>
<nav class="abs nav">
  <ul class="nav-list">
    <li class="home"><svg width="16" height="16" viewBox="0 0 16 16" aria-label="Home"><path d="M8 1 1 8h2v7h4v-4h2v4h4V8h2z" fill="#14b3c4"/></svg></li>
    <li>PRODUCTS</li><li>SERVICE</li><li class="active">SUPPORT</li><li>ABOUT</li><li>CONTACT</li>
  </ul>
</nav>
<section class="abs hero">
  <div class="abs hero-visual" role="img" aria-label="Tablet and phone showing the monitoring dashboard"></div>
  <div class="abs slide-tabs"><span>1</span><span>2</span><span class="current">3</span><span>4</span></div>
  <div class="abs hero-title"><h1>TABLET</h1><h2>COMING SOON !!</h2></div>
  <p class="abs hero-copy">A Tablet version of q.Insight for Gridwatch® will be released in August. You will see the same great features as in the phone version.</p>
</section>
<div class="abs dropdown"><span>Customer Portal</span></div>
<main>
  <section class="abs col" style="left:169px">
    <h2 class="col-head">VIDEOS &amp; DATASHEETS</h2>
    <ul class="videos">
      <li><b>q.Insight</b><small>Dynamic video about our q.Insight application.</small></li>
      <li><b>q.Insight Datasheet</b><small>Download the q.Insight Datasheet.</small></li>
      <li><b>HCD/C</b><small>HCD/C Feature Presentation</small></li>
      <li><b>HCD/C Datasheet</b><small>Download the HCD/C Datasheet</small></li>
    </ul>
  </section>
  <section class="abs col" style="left:368px">
    <h2 class="col-head">SUPPORT</h2>
    <div class="support-photo" role="img" aria-label="Support agent with headset in an office"></div>
    <div class="support-box">We provide several levels of support for our software and we do not follow strict support levels. You decide, what level of support you need.<br><span class="btn">READ MORE</span></div>
  </section>
  <section class="abs col" style="left:566px">
    <h2 class="col-head">NEWS</h2>
    <div class="news">
      <h3>HCD/C Released</h3><time>2013-05-21</time>
      <p>Varno-Labs has released the first version of the Halcyon Cloud Director Collector for Kestrel Gridwatch. The collector is natively integrated into the Gridwatch installation and comes with a rich set of reports.</p>
      <h3>HCD/C Released</h3><time>2013-05-21</time>
      <p>A Tablet version of q.Insight for Gridwatch will be released in August. You will see the same great features as in the phone version.</p>
    </div>
  </section>
  <section class="abs col" style="left:765px">
    <h2 class="col-head">TESTIMONIALS</h2>
    <blockquote class="quote"><span class="mark open">“</span><span class="mark close">”</span><p>Lorem ipsum dolor sit amet, consectetur adipisicing...</p><cite>Aloe Doe</cite></blockquote>
    <blockquote class="quote" style="margin-top:28px"><span class="mark open">“</span><span class="mark close">”</span><p>Lorem ipsum dolor sit amet, consectetur adipisicing...</p><cite>John Doe</cite></blockquote>
  </section>
</main>
<section class="abs gallery">
  <h2 class="abs gallery-label">GALLERY</h2>
  <svg class="abs arrow" style="left:170px" width="16" height="26" viewBox="0 0 16 26"><path d="M14 2 3 13l11 11" stroke="#555" stroke-width="3" fill="none"/></svg>
  <div class="abs thumb" style="left:218px" role="img" aria-label="Events dashboard screenshot"></div>
  <div class="abs thumb" style="left:394px" role="img" aria-label="Device summary screenshot"></div>
  <div class="abs thumb" style="left:571px" role="img" aria-label="Inventory screenshot"></div>
  <div class="abs thumb" style="left:747px" role="img" aria-label="Network summary screenshot"></div>
  <svg class="abs arrow" style="left:934px" width="16" height="26" viewBox="0 0 16 26"><path d="M2 2l11 11L2 24" stroke="#555" stroke-width="3" fill="none"/></svg>
</section>
<footer class="abs footer">Copyright © 2013 Varno-Labs<br>Kestrel, Gridwatch are either registered trademarks or trademarks of Kestrel Corporation in the United States and/or other countries.</footer>
</body>
</html>
```